Electrical needs letterhead design

Need a letterhead design for an electrical company. Using the same colours as to what are used in the logo.
After a modern design.

Want the logo in top right or top left.

Must include...

ABN 61 842 307 194
PHONE 0492357018
www.voltarnex.com.au
ben@voltarnex.com.au

'ABN' and 'PHONE' in bold.

Keep it basic. Logo top left, details either next to it or far right corner. Dont want any other objects included.

```html
<!DOCTYPE html>
<html lang="en">
<head>
<meta charset="utf-8">
<title>Voltarnex Letterhead</title>
<link rel="stylesheet" href="https://fonts.googleapis.com/css2?family=Open+Sans:wght@400;600;700&display=swap">
<style>
  :root {
    --backdrop: #8f8f8f;
    --paper: #ffffff;
    --brand-red: #88221f;
    --rule-grey: #b9b9b9;
    --footer-text: #ffffff;
  }
  * { box-sizing: border-box; margin: 0; padding: 0; }
  html, body {
    width: 1200px;
    height: 640px;
    overflow: hidden;
    background: var(--backdrop);
  }
  .canvas {
    position: relative;
    width: 1200px;
    height: 640px;
  }
  .letterhead {
    position: absolute;
    left: 388px;
    top: 20px;
    width: 425px;
    height: 600px;
    background: var(--paper);
    box-shadow: 0 1px 3px rgba(0, 0, 0, 0.35);
    font-family: "Open Sans", sans-serif;
  }
  .brand {
    position: absolute;
    left: 37px;
    top: 44px;
    display: flex;
    align-items: center;
    gap: 7px;
  }
  .brand-dot {
    width: 12px;
    height: 12px;
    border-radius: 50%;
    background: var(--brand-red);
  }
  .brand-name {
    font-size: 26px;
    font-weight: 400;
    line-height: 1;
    color: var(--brand-red);
    letter-spacing: -0.2px;
  }
  .header-rule {
    position: absolute;
    left: 180px;
    right: 0;
    top: 76px;
    height: 1px;
    background: var(--rule-grey);
  }
  .contact-band {
    position: absolute;
    left: 0;
    right: 0;
    bottom: 0;
    height: 30px;
    background: var(--brand-red);
    color: var(--footer-text);
    text-align: center;
    padding-top: 5px;
  }
  .contact-line {
    font-size: 7px;
    line-height: 10px;
    white-space: nowrap;
  }
  .contact-line.secondary { font-size: 5.6px; line-height: 9px; }
  .contact-line strong { font-weight: 700; }
  .divider { margin: 0 3px; }
</style>
</head>
<body>
  <main class="canvas">
    <article class="letterhead">
      <header class="brand">
        <span class="brand-dot" aria-hidden="true"></span>
        <span class="brand-name">Voltarnex</span>
      </header>
      <div class="header-rule"></div>
      <footer class="contact-band">
        <p class="contact-line"><strong>T.</strong> 0492357018<span class="divider">|</span><strong>E.</strong> ben@voltarnex.com.au</p>
        <p class="contact-line secondary">www.voltarnex.com.au<span class="divider">|</span><strong>ABN</strong> 61 842 307 194</p>
      </footer>
    </article>
  </main>
</body>
</html>
```